Marta Quinlan Photography needs a unique, creative business card/logo design

I need a design for business cards/logo that is unique and creative in the industry. Simplicity is nice, so not too crowded. Something that will catch my customer's eye and remain in their memory. I am primarily a landscape photographer but will be soon may be branching into boudoir photography as well. I have attached my current card.

Industry/Entity Type

Business

Contact Information for Business Card

Marta Quinlan Photography
Phone: 0439 271 504
Email: MartaQuinlanPhotography@brivomail.net
Website: www.pagerly.net/MartaQuinlanPhotography.Aust

Logo Text

Marta Quinlan Photography

Requirements
Must have
• Contact Details on one side
Should not have
• pixelation

```html
<!DOCTYPE html>
<html lang="en">
<head>
<meta charset="utf-8">
<title>Marta Quinlan Photography – Business Card</title>
<link rel="stylesheet" href="https://fonts.googleapis.com/css2?family=Open+Sans:wght@400;700&display=swap">
<style>
  :root {
    --backdrop: #3a322d;
    --card: #1b1b1b;
    --silver: #a8a8a8;
    --orange: #f26b1d;
    --cyan: #1ea7e6;
    --ink-light: #f2f2f2;
  }
  * { margin: 0; padding: 0; box-sizing: border-box; }
  html, body { width: 1200px; height: 780px; overflow: hidden; }
  body {
    background: var(--backdrop);
    font-family: "Open Sans", Arial, sans-serif;
    position: relative;
  }
  .card {
    position: absolute;
    width: 540px;
    height: 310px;
    background: var(--card);
    border-radius: 4px;
    box-shadow: 0 12px 30px rgba(0,0,0,.45);
    overflow: hidden;
  }
  .card--front { left: 60px; top: 70px; }
  .card--back  { left: 600px; top: 400px; }

  /* front */
  .front-brand {
    position: absolute;
    left: 0; right: 0; top: 100px;
    display: flex; flex-direction: column; align-items: center; gap: 16px;
  }
  .front-brand__dot {
    width: 46px; height: 46px; border-radius: 50%;
    background: var(--silver);
  }
  .front-brand__name {
    color: var(--silver);
    font-size: 24px; font-weight: 400; letter-spacing: .5px;
  }

  /* back */
  .holder-name {
    position: absolute; left: 34px; top: 70px;
    color: var(--cyan); font-size: 19px; font-weight: 700;
  }
  .rule {
    position: absolute; height: 1px; background: var(--orange);
  }
  .rule--name { left: 34px; top: 102px; width: 310px; }
  .rule--brand { left: 350px; top: 232px; width: 170px; }
  .contact-list {
    position: absolute; left: 34px; top: 118px;
    list-style: none;
  }
  .contact-list li {
    display: flex; align-items: center; gap: 8px;
    color: var(--ink-light); font-size: 12.5px; line-height: 24px;
  }
  .contact-list svg { width: 12px; height: 12px; flex: none; }
  .back-brand {
    position: absolute; left: 350px; top: 110px; width: 170px;
    display: flex; flex-direction: column; align-items: center; gap: 12px;
  }
  .back-brand__dot {
    width: 44px; height: 44px; border-radius: 50%;
    background: var(--orange);
  }
  .back-brand__name {
    color: var(--cyan); font-size: 17px; font-weight: 400;
    text-align: center; line-height: 1.2;
  }
</style>
</head>
<body>

<section class="card card--front" aria-label="Card front">
  <div class="front-brand">
    <span class="front-brand__dot"></span>
    <span class="front-brand__name">Marta Quinlan Photography</span>
  </div>
</section>

<section class="card card--back" aria-label="Card back">
  <h1 class="holder-name">Your Name</h1>
  <div class="rule rule--name"></div>
  <ul class="contact-list">
    <li>
      <svg viewBox="0 0 12 12" fill="none" stroke="var(--orange)" stroke-width="1.2"><rect x="3" y="0.8" width="6" height="10.4" rx="1"/><line x1="5.2" y1="9.4" x2="6.8" y2="9.4"/></svg>
      0439 271 504
    </li>
    <li>
      <svg viewBox="0 0 12 12" fill="none" stroke="var(--orange)" stroke-width="1.2"><rect x="0.8" y="2.5" width="10.4" height="7" rx="0.8"/><polyline points="0.8,2.8 6,6.6 11.2,2.8"/></svg>
      MartaQuinlanPhotography@brivomail.net
    </li>
    <li>
      <svg viewBox="0 0 12 12" fill="none" stroke="var(--orange)" stroke-width="1.1"><circle cx="6" cy="6" r="5.2"/><ellipse cx="6" cy="6" rx="2.3" ry="5.2"/><line x1="0.8" y1="6" x2="11.2" y2="6"/></svg>
      www.pagerly.net/MartaQuinlanPhotography.Aust
    </li>
  </ul>
  <div class="back-brand">
    <span class="back-brand__dot"></span>
    <span class="back-brand__name">Marta Quinlan Photography</span>
  </div>
  <div class="rule rule--brand"></div>
</section>

</body>
</html>
```